CREATIVE DESIGNERS NEEDED & Enhance Your Business Card Portfolio

Artistic, unique, professional real estate card needed - see attached documents "B-cards.pdf" for all details and examples.True Designers will see other projects of ours come online here. We like long-term relationships for creative designers. This business card will be used in two U.S. states and is central to our business and other future marketing.

Target Market(s)

Buyers and Sellers of real estate

Industry/Entity Type

Real Estate Agent

Contact Information for Business Card

See attached detailed brief

Other font styles liked:
• ADAM.CG PRO & NewsGoth BT

Requirements
Must have
• 2-sided, creative (non-traditional layout/design). Incorporate a cut-out (for texture, and make it fun! No boring templates for this card -
Nice to have
• See attached detailed brief
Should not have

```html
<!DOCTYPE html>
<html lang="en">
<head>
<meta charset="utf-8">
<title>Hollis Group – Business Card Concepts</title>
<link href="https://fonts.googleapis.com/css2?family=Roboto+Condensed:wght@300;400;700&family=Sorts+Mill+Goudy&family=PT+Sans:wght@700&display=swap" rel="stylesheet">
<style>
  :root {
    --paper: #ffffff;
    --frame: #4a4a4a;
    --brand-red: #e8323a;
    --brand-navy: #26323f;
    --bar: #231f20;
    --ink: #3d3d3d;
    --ink-soft: #4a4a4a;
    --photo-dark: #3a3a3a;
    --photo-light: #c8c8c8;
  }
  * { box-sizing: border-box; margin: 0; padding: 0; }
  html, body {
    width: 1200px;
    height: 1200px;
    overflow: hidden;
    background: var(--paper);
  }
  .sheet {
    position: relative;
    width: 1200px;
    height: 1200px;
    border: 1.5px solid var(--frame);
    background: var(--paper);
  }
  .card {
    position: absolute;
    left: 185px;
    width: 898px;
    height: 448px;
    border: 1px solid var(--frame);
    background: var(--paper);
    overflow: hidden;
  }
  .card--first { top: 81px; }
  .card--second { top: 656px; }

  .brand {
    position: absolute;
    left: 150px;
    top: 78px;
    display: flex;
    align-items: center;
    gap: 16px;
  }
  .brand__mark {
    width: 34px;
    height: 34px;
    background: var(--brand-red);
  }
  .brand__name {
    font-family: "Roboto Condensed", sans-serif;
    font-weight: 700;
    font-size: 54px;
    line-height: 1;
    letter-spacing: 1px;
    color: var(--brand-red);
  }
  .locations {
    position: absolute;
    left: 320px;
    top: 152px;
    font-family: "Sorts Mill Goudy", serif;
    font-size: 30px;
    color: var(--ink-soft);
    white-space: nowrap;
  }
  .tagline {
    position: absolute;
    left: 0;
    top: 232px;
    width: 704px;
    height: 32px;
    display: flex;
    align-items: center;
  }
  .tagline__bar {
    height: 23px;
    background: var(--bar);
  }
  .tagline__bar--left { width: 87px; }
  .tagline__bar--right { width: 92px; margin-left: 3px; }
  .tagline__text {
    font-family: "Roboto Condensed", sans-serif;
    font-weight: 300;
    font-size: 32.5px;
    color: var(--ink);
    white-space: nowrap;
    margin-left: 8px;
    line-height: 1;
  }
  .agent {
    position: absolute;
    left: 232px;
    top: 328px;
  }
  .agent__name {
    font-family: "PT Sans", sans-serif;
    font-weight: 700;
    font-size: 40px;
    letter-spacing: 1.5px;
    word-spacing: 14px;
    color: var(--ink-soft);
    line-height: 1.1;
  }
  .agent__title {
    font-family: "Roboto Condensed", sans-serif;
    font-weight: 400;
    font-size: 21px;
    color: var(--ink);
    margin-top: 4px;
  }
  .portrait {
    position: absolute;
    right: 0;
    top: 0;
    width: 240px;
    height: 448px;
    background: linear-gradient(160deg, var(--photo-dark) 0%, #8a8a8a 35%, var(--photo-light) 60%, #6e6e6e 100%);
    clip-path: polygon(16% 0, 100% 0, 100% 100%, 0 100%, 22% 95%, 18% 80%, 12% 60%, 18% 42%, 24% 30%, 20% 12%);
  }
</style>
</head>
<body>
<main class="sheet">
  <section class="card card--first">
    <div class="brand">
      <span class="brand__mark"></span>
      <span class="brand__name">HOLLIS GROUP</span>
    </div>
    <p class="locations">San Diego &amp; Phoenix</p>
    <div class="tagline">
      <span class="tagline__bar tagline__bar--left"></span>
      <span class="tagline__text">Residential. Investment. Development</span>
      <span class="tagline__bar tagline__bar--right"></span>
    </div>
    <div class="agent">
      <h1 class="agent__name">Dan Hollis</h1>
      <p class="agent__title">Broker Associate &amp; Realtor</p>
    </div>
    <div class="portrait" role="img" aria-label="Posterized black and white portrait of the agent, cropped at the right edge"></div>
  </section>

  <section class="card card--second">
    <div class="brand">
      <span class="brand__mark"></span>
      <span class="brand__name">HOLLIS GROUP</span>
    </div>
    <p class="locations">San Diego &amp; Phoenix</p>
    <div class="tagline">
      <span class="tagline__bar tagline__bar--left"></span>
      <span class="tagline__text">Residential. Investment. Development</span>
      <span class="tagline__bar tagline__bar--right"></span>
    </div>
    <div class="agent">
      <h2 class="agent__name">Dan Hollis</h2>
      <p class="agent__title">Broker Associate &amp; Realtor</p>
    </div>
    <div class="portrait" role="img" aria-label="Posterized black and white portrait of the agent, cropped at the right edge"></div>
  </section>
</main>
</body>
</html>
```